Pricing and Packages Page

#1 Just looking for a design no coding
We Are looking for a Design of the PRICING AND PACKAGES page. The home page is just for reference material.
Winner will be contacted and possibly hired to do additional jobs.
Brivo Real Estate needs a web page design for our bundles. We need it to be visually appeal and an emphasis placed on the premium bundle. Attached are some pngs of our current page, and a paint mock up of an idea of our layout. Please try and stay within the theme of the top menu bars of the paint file. Whites, Blues, Oranges, and Light Grays would be preferred.
Provided is a mock-up of our home screen. We want easy to read yet an initiative for people to select home listing packages on our website. Possible reference websites would be dwellmart.example and listyourplace.example or any website that has packages and pricing to choose from.
The top of the page should include the title Packages & Pricing.
Below that we want to have it easily read and illustrated that the will "Pay Nothing Until Home Sold"
Next to that a space to enter a anticipated sales price, asking the question, how much will you save. Much sure this is emphasized.
Include the bundles, which are separated into three packages, Basic, Premium and Multi-List Package. Please include the Bundle Prices of $179, $249 and $499 along with + Transaction Coordination Fee $299. Have a spot for a Get Started Button.
The boxes on the side are just an example of what to include with the prices.
Transaction Coordination Fee and All Listings Include, We just want the text display in a way where the page isnt text heavy but illustrated.
Additional Services Offered, Just a basic list with prices next to it.
Paint

```html
<!DOCTYPE html>
<html lang="en">
<head>
<meta charset="utf-8">
<title>Brivo Real Estate – Packages &amp; Pricing</title>
<link rel="stylesheet" href="https://fonts.googleapis.com/css2?family=Open+Sans:wght@400;600;700&display=swap">
<style>
:root{
  --navy:#0d3f86;
  --blue:#1657a8;
  --blue-mid:#1f63b5;
  --blue-deep:#0a3270;
  --sky:#2b73c2;
  --orange:#f5821f;
  --orange-dark:#e06d0c;
  --panel:#f4f4f4;
  --panel-line:#ffffff;
  --card:#f2f2f2;
  --card-border:#e0e0e0;
  --ink:#2b2b2b;
  --muted:#555;
  --white:#fff;
}
*{box-sizing:border-box;margin:0;padding:0}
html,body{width:1200px;height:2817px;overflow:hidden}
body{font-family:"Open Sans",Arial,sans-serif;color:var(--ink);background:var(--white);position:relative}
.abs{position:absolute}

/* top bar */
.topbar{left:0;top:0;width:1200px;height:34px;background:var(--navy)}
.topnav{left:118px;top:0;height:34px;display:flex;gap:34px;align-items:center;font-size:12px;color:var(--white);text-transform:uppercase}
.topphone{left:812px;top:0;height:34px;line-height:34px;font-size:14px;font-weight:700;color:var(--white)}
.tophelp{left:916px;top:0;width:164px;height:34px;background:var(--orange);color:var(--white);font-size:11px;line-height:34px;text-align:center;text-transform:uppercase}

/* header */
.brand{left:122px;top:52px;display:flex;align-items:center;gap:8px;font-size:24px;font-weight:600;color:var(--blue)}
.brand-mark{width:28px;height:28px;background:var(--orange);border-radius:3px}
.user{left:928px;top:46px;width:152px;height:40px;background:#e8e8e8;border-radius:20px 4px 4px 20px;display:flex;align-items:center;gap:10px;font-size:12px;font-weight:700;color:#333}
.avatar{width:40px;height:40px;border-radius:50%;background:linear-gradient(#c9a58a,#7a5a48);border:2px solid #fff}
.user .caret{margin-left:10px;font-size:9px;color:#666}

/* pricing banner */
.banner{left:195px;top:141px;width:810px;height:191px;border:3px solid var(--orange);border-radius:10px;overflow:hidden;background:linear-gradient(var(--blue-mid),var(--blue-deep))}
.banner-head{height:52px;background:var(--blue);border-bottom:1px solid #4b86cc;display:flex;justify-content:space-between;align-items:center;padding:0 20px 0 10px;color:var(--white)}
.banner-head h1{font-size:23px;font-weight:700}
.banner-head p{font-size:16px}
.banner-body{display:flex;height:133px}
.pay{width:246px;border-right:1px solid #4b86cc;display:flex;align-items:center;padding-left:12px;gap:14px;color:var(--white)}
.pay .zero{font-size:52px;font-weight:400;line-height:1}
.pay strong{display:block;font-size:22px;font-weight:700;line-height:1.1}
.pay span{font-size:17px}
.save{padding:14px 0 0 24px;color:var(--white)}
.save h2{font-size:24px;font-weight:700;margin-bottom:6px}
.save-row{display:flex;gap:12px;align-items:center}
.save-input{width:358px;height:36px;background:#0a3a78;border:1px solid #3b72b8;font-size:22px;padding-left:10px;line-height:34px}
.save-btn{width:120px;height:38px;background:var(--orange);font-size:16px;font-weight:700;text-align:center;line-height:38px}
.save small{display:block;font-size:12px;margin-top:6px}

/* plans */
.plans{left:195px;top:357px;width:810px;height:958px;background:var(--panel)}
.plans-title{position:absolute;top:20px;width:100%;text-align:center;font-size:24px;font-weight:700;color:var(--navy)}
.plans-grid{position:absolute;top:63px;left:0;display:grid;grid-template-columns:228px repeat(3,194px);grid-template-rows:106px 94px 109px 79px 93px 184px 79px 79px 72px}
.cell{display:flex;align-items:center;justify-content:center;font-size:13px;border-bottom:2px solid var(--panel-line)}
.cell.label{justify-content:flex-start;padding-left:21px;line-height:1.9}
.plan-name-row .cell{border-bottom:none;flex-direction:column}
.plan-label{font-size:22px;font-weight:700;color:var(--navy)}
.plan-tier{font-size:15px;font-weight:700;color:var(--orange)}
.plan-price{font-size:30px;color:var(--blue)}
.cell.last{border-bottom:none}
.mark{width:26px;height:26px}
.partner-block{display:block}
.partner-names{margin-top:8px;font-size:20px;font-weight:700;color:var(--navy);line-height:1.4}
.start-btn{width:128px;height:34px;background:var(--orange);border-radius:4px;color:var(--white);font-size:13px;font-weight:600;text-align:center;line-height:34px}
.note{left:197px;top:1332px;font-size:12px;font-weight:700;color:#111}

/* transaction */
.tc{left:195px;top:1371px;width:810px;height:147px;border:3px solid var(--orange);border-radius:10px;overflow:hidden;background:linear-gradient(var(--blue-mid),var(--blue-deep))}
.tc-head{height:45px;background:var(--blue);border-bottom:1px solid #4b86cc;padding-left:18px;line-height:44px;color:var(--white);font-size:16px;font-weight:700;font-style:italic}
.tc-body{display:flex;align-items:center;height:96px;color:var(--white)}
.tc-no{width:120px;text-align:center;line-height:1}
.tc-no b{display:block;font-size:44px;font-weight:700}
.tc-no span{font-size:19px;font-weight:700}
.tc-body p{font-size:16px;line-height:1.6;width:600px;margin-left:30px}

/* features */
.features-title{left:198px;top:1566px;font-size:22px;color:var(--sky)}
.feature{width:397px;height:141px;background:var(--card);border:1px solid var(--card-border);border-radius:4px;display:flex;align-items:center;padding-left:16px;gap:24px}
.feature-icon{width:113px;height:113px;border-radius:50%;background:var(--navy);display:flex;align-items:center;justify-content:center;flex:none}
.feature p{font-size:16px;color:#444;line-height:1.6}

/* services */
.svc-title{left:199px;top:2093px;font-size:17px;font-weight:700;color:var(--orange)}
.svc-sub{left:201px;top:2118px;font-size:10px;color:#333}
.svc{left:195px;top:2152px;width:810px;height:355px;background:var(--panel)}
.svc-q{height:64px;border-bottom:2px solid var(--white);padding-left:22px;display:flex;align-items:center;gap:12px;font-size:16px;font-weight:700;color:var(--navy)}
.svc-q i{width:14px;height:14px;border:1.5px solid var(--navy);background:var(--white)}
.svc-row{display:grid;grid-template-columns:326px 200px 284px;align-items:center;padding-left:22px;font-size:16px;border-bottom:2px solid var(--white)}
.svc-row.head{height:56px;font-size:15px;font-weight:700;color:var(--navy)}
.svc-row.item{height:59px}
.svc-row.item:last-child{border-bottom:none}
.svc-row .add{text-align:center}

/* footer */
.skyline{left:0;top:2539px;width:1200px;height:30px;background:linear-gradient(transparent 0,transparent 30%,var(--blue) 30%)}
.footer{left:0;top:2567px;width:1200px;height:193px;background:var(--blue)}
.fcol{top:2623px;display:flex;flex-direction:column;font-size:11px;color:var(--white)}
.fcol a{display:block;width:145px;height:21px;line-height:20px;border-bottom:1px solid #3f7cc4;color:inherit;text-decoration:none}
.news-label{left:779px;top:2621px;font-size:11px;color:var(--white)}
.news-input{left:779px;top:2644px;width:267px;height:31px;background:var(--white)}
.news-btn{left:1046px;top:2644px;width:34px;height:31px;background:var(--orange);display:flex;align-items:center;justify-content:center}
.social{left:779px;top:2700px;display:flex;gap:6px}
.social i{width:28px;height:28px;background:#2d6db8;border:1px solid #5d93d1}
.bottombar{left:0;top:2760px;width:1200px;height:57px;background:var(--blue-deep);color:#c6d7ef;font-size:10px}
.bottombar .copy{position:absolute;left:120px;top:22px}
.bottombar .powered{position:absolute;right:120px;top:22px}
</style>
</head>
<body>
<svg width="0" height="0" style="position:absolute">
  <symbol id="mark" viewBox="0 0 26 26">
    <circle cx="13" cy="13" r="13" fill="#0d3f86"/>
    <path d="M8.5 8.5l9 9M17.5 8.5l-9 9" stroke="#fff" stroke-width="2.8" stroke-linecap="round"/>
  </symbol>
</svg>

<div class="abs topbar"></div>
<nav class="abs topnav"><span>Search Listings</span><span>Why Choose Brivo</span><span>Directory</span><span>Guides</span></nav>
<div class="abs topphone">+ 954-555-0187</div>
<div class="abs tophelp">FAQ'S / Contact Us / Help</div>

<div class="abs brand"><span class="brand-mark"></span>Brivo Real Estate</div>
<div class="abs user"><span class="avatar" role="img" aria-label="User profile photo"></span>MARIN K.<span class="caret">▼</span></div>

<section class="abs banner">
  <div class="banner-head"><h1>Packaging &amp; Pricing</h1><p>Maximum Market Exposure Guaranteed !</p></div>
  <div class="banner-body">
    <div class="pay"><span class="zero">$0</span><div><strong>Pay Nothing</strong><span>Until Home Sold</span></div></div>
    <div class="save">
      <h2>How Much Will You Save?</h2>
      <div class="save-row"><div class="save-input">$</div><div class="save-btn">My Savings</div></div>
      <small>Enter Estimated Sales Price</small>
    </div>
  </div>
</section>

<section class="abs plans">
  <h2 class="plans-title">Most Popular</h2>
  <div class="plans-grid">
    <div class="cell label plan-name-row" style="border:none"><span class="plan-label">Plans</span></div>
    <div class="cell" style="border:none;flex-direction:column"><span class="plan-tier">Basic</span><span class="plan-price">$199</span></div>
    <div class="cell" style="border:none;flex-direction:column"><span class="plan-tier">Premium</span><span class="plan-price">$249</span></div>
    <div class="cell" style="border:none;flex-direction:column"><span class="plan-tier">MLS</span><span class="plan-price">$449</span></div>

    <div class="cell label">Listing On brivorealestate.example</div>
    <div class="cell"><svg class="mark"><use href="#mark"/></svg></div>
    <div class="cell"><svg class="mark"><use href="#mark"/></svg></div>
    <div class="cell"><svg class="mark"><use href="#mark"/></svg></div>

    <div class="cell label">Earn Featured Listing<br>on brivorealestate.example</div>
    <div class="cell"><svg class="mark"><use href="#mark"/></svg></div>
    <div class="cell"><svg class="mark"><use href="#mark"/></svg></div>
    <div class="cell"><svg class="mark"><use href="#mark"/></svg></div>

    <div class="cell label">Photos</div>
    <div class="cell">6</div>
    <div class="cell">Unlimited</div>
    <div class="cell">Unlimited</div>

    <div class="cell label">Free Brokers Price Opinion</div>
    <div class="cell"></div>
    <div class="cell"><svg class="mark"><use href="#mark"/></svg></div>
    <div class="cell"><svg class="mark"><use href="#mark"/></svg></div>

    <div class="cell label"><div class="partner-block">Exposure on over 50+ real estate<br>websites including<div class="partner-names">Homevista &nbsp;Nestly<br>Roofline Homes</div></div></div>
    <div class="cell"></div>
    <div class="cell"><svg class="mark"><use href="#mark"/></svg></div>
    <div class="cell"><svg class="mark"><use href="#mark"/></svg></div>

    <div class="cell label">Premium Yard Sign with<br>Mobile ID#</div>
    <div class="cell"></div>
    <div class="cell"><svg class="mark"><use href="#mark"/></svg></div>
    <div class="cell"><svg class="mark"><use href="#mark"/></svg></div>

    <div class="cell label">Listing On Local MLS</div>
    <div class="cell"></div>
    <div class="cell"></div>
    <div class="cell"><svg class="mark"><use href="#mark"/></svg></div>

    <div class="cell last"></div>
    <div class="cell last"><span class="start-btn">Get Started</span></div>
    <div class="cell last"><span class="start-btn">Get Started</span></div>
    <div class="cell last"><span class="start-btn">Get Started</span></div>
  </div>
</section>
<p class="abs note">*This requires 3% buyers agent comission</p>

<section class="abs tc">
  <div class="tc-head">Transaction Coordination fee</div>
  <div class="tc-body">
    <div class="tc-no"><b>NO</b><span>Worries</span></div>
    <p>As the transaction coordinators,Brivo Real Estate will guide the buyer an seller through the entire transaction in an efficient and worry free way</p>
  </div>
</section>

<h2 class="abs features-title">All Listings Include</h2>
<div class="abs feature" style="left:195px;top:1617px">
  <div class="feature-icon"><svg width="44" height="44" viewBox="0 0 44 44"><circle cx="22" cy="14" r="9" fill="#fff"/><path d="M5 40c0-10 8-15 17-15s17 5 17 15z" fill="#fff"/></svg></div>
  <p>Only Pre- Approved Buyers</p>
</div>
<div class="abs feature" style="left:608px;top:1617px">
  <div class="feature-icon"><svg width="46" height="46" viewBox="0 0 46 46"><path d="M23 5L3 22h6v18h28V22h6z" fill="#fff"/><rect x="19" y="28" width="8" height="12" fill="#0d3f86"/><rect x="20" y="18" width="6" height="5" fill="#0d3f86"/></svg></div>
  <p>Schedule Open Houses</p>
</div>
<div class="abs feature" style="left:195px;top:1780px">
  <div class="feature-icon"><svg width="52" height="44" viewBox="0 0 52 44"><ellipse cx="22" cy="17" rx="19" ry="13" fill="#fff"/><path d="M10 27l-4 9 11-6z" fill="#fff"/><ellipse cx="33" cy="25" rx="16" ry="11" fill="#fff" stroke="#0d3f86" stroke-width="2"/><path d="M42 33l5 8-11-5z" fill="#fff"/></svg></div>
  <p>Customers Support 7days a<br>week via E- mail,Phone &amp; Chat</p>
</div>
<div class="abs feature" style="left:608px;top:1780px">
  <div class="feature-icon"><svg width="40" height="48" viewBox="0 0 40 48"><rect x="3" y="6" width="34" height="40" rx="3" fill="#fff"/><rect x="13" y="2" width="14" height="8" rx="2" fill="#fff" stroke="#0d3f86" stroke-width="2"/><path d="M10 18h20M10 25h20M10 32h20M10 39h14" stroke="#0d3f86" stroke-width="2.5"/></svg></div>
  <p>Contract Negotiation Support</p>
</div>
<div class="abs feature" style="left:195px;top:1942px">
  <div class="feature-icon"><svg width="46" height="46" viewBox="0 0 46 46"><path d="M8 38L30 16" stroke="#fff" stroke-width="6" stroke-linecap="round"/><circle cx="33" cy="12" r="8" fill="#fff"/><circle cx="36" cy="9" r="4" fill="#0d3f86"/><path d="M10 8l28 28" stroke="#fff" stroke-width="5" stroke-linecap="round"/><rect x="4" y="4" width="10" height="6" rx="2" fill="#fff" transform="rotate(45 9 7)"/></svg></div>
  <p>Step by Step<br>Guides &amp; Tools</p>
</div>
<div class="abs feature" style="left:608px;top:1942px">
  <div class="feature-icon"><svg width="36" height="46" viewBox="0 0 36 46"><path d="M2 2h22l10 10v32H2z" fill="#fff"/><path d="M8 18h20M8 25h20M8 32h20M8 39h14" stroke="#0d3f86" stroke-width="2.5"/></svg></div>
  <p>Listing Stat Tracking</p>
</div>

<h3 class="abs svc-title">Additional Services Offered</h3>
<p class="abs svc-sub">Payment Due when services is completed</p>
<section class="abs svc">
  <div class="svc-q">Will you offer a 3% buyers agent commission <i></i></div>
  <div class="svc-row head"><span>Service</span><span>Price</span><span></span></div>
  <div class="svc-row item"><span>Professional Photography</span><span>$ XXX</span><span class="add">Add</span></div>
  <div class="svc-row item"><span>Professional House Staging</span><span>$ XXX</span><span class="add">Add</span></div>
  <div class="svc-row item"><span>Broker Price Opinion</span><span>$ XXX</span><span class="add">Add</span></div>
  <div class="svc-row item"><span>Premium Yard Sign</span><span>$ XXX</span><span class="add">Add</span></div>
</section>

<div class="abs skyline" role="img" aria-label="City skyline silhouette"></div>
<footer class="abs footer"></footer>
<div class="abs fcol" style="left:120px"><a>About</a><a>Research</a><a>Services</a><a>Contact Us</a><a>Why Choose Us</a></div>
<div class="abs fcol" style="left:332px"><a>Search Listings</a><a>Real Estate Guides</a><a>Neighborhood Info</a><a>Get Pre-Approved</a><a>Fair Housing Laws &amp; Information</a></div>
<div class="abs fcol" style="left:541px"><a>Disclaimers</a><a>Feedback</a><a>Terms &amp; Conditions</a><a>Help</a></div>
<p class="abs news-label">Enter your email adress to sign for our newsletter.</p>
<div class="abs news-input"></div>
<div class="abs news-btn"><svg width="18" height="14" viewBox="0 0 18 14"><path d="M1 7h14M10 2l5 5-5 5" stroke="#fff" stroke-width="2.5" fill="none"/></svg></div>
<div class="abs social"><i></i><i></i><i></i><i></i><i></i></div>
<div class="abs bottombar"><span class="copy">© 2014 Brivo Real Estate &nbsp;|&nbsp; All rights reserved.</span><span class="powered">Powered by Velto Technologies Ltd</span></div>
</body>
</html>
```